Consulting group
Business cards and stationary
Use same font as used in my logo
I think it is Swiss721?
Simple
Damon Fairley
President
417 W. Marlow Avenue, Apt 118 Ann Arbor, MI 48177
Damon@DamonFairley.com
www.TheCopperLantern.com
Looking for envelope, letterhead, and business card.
the logo? if you want to try putting a quote on it: "“The worst thing that can happen to a good cause is, not to be skillfully attacked, but to be ineptly defended.” - Corvelle. Not sure if I will like the quote on there or not.

```html
<!DOCTYPE html>
<html lang="en">
<head>
<meta charset="utf-8">
<title>The Copper Lantern — Business Card</title>
<link href="https://fonts.googleapis.com/css2?family=Archivo:wght@400;700;800&family=Arimo:wght@400;700&display=swap" rel="stylesheet">
<style>
  :root {
    --canvas: #e6e6e6;
    --brand-red: #c8101f;
    --brand-red-dark: #8e0a14;
    --paper: #ffffff;
    --ink: #111111;
    --on-red: #ffffff;
    --on-red-soft: #f6d6d9;
  }
  * { box-sizing: border-box; margin: 0; padding: 0; }
  html, body { width: 1200px; height: 901px; overflow: hidden; }
  body {
    background: var(--canvas);
    display: flex;
    align-items: center;
    justify-content: center;
    gap: 40px;
    font-family: "Arimo", Arial, sans-serif;
  }
  .card {
    width: 540px;
    height: 309px;
    border-radius: 0 46px 0 46px;
    overflow: hidden;
    position: relative;
    box-shadow: 0 6px 18px rgba(0,0,0,.18);
  }

  /* Front */
  .card--front { display: flex; background: var(--paper); }
  .front__brand {
    width: 310px;
    display: flex;
    align-items: center;
    gap: 18px;
    padding-left: 34px;
  }
  .brand-square {
    width: 50px; height: 50px;
    background: var(--brand-red);
    flex: none;
  }
  .brand-name {
    font-family: "Archivo", Arial, sans-serif;
    font-weight: 800;
    font-size: 28px;
    line-height: 1.02;
    color: var(--ink);
    letter-spacing: -0.3px;
  }
  .front__divider {
    width: 10px;
    background: var(--brand-red-dark);
    border-left: 3px solid var(--paper);
    border-right: 3px solid var(--paper);
    background-clip: padding-box;
  }
  .front__details {
    flex: 1;
    background: var(--brand-red);
    color: var(--on-red);
    padding: 28px 18px 18px 20px;
    display: flex;
    flex-direction: column;
  }
  .person-name { font-weight: 700; font-size: 17px; }
  .address { margin-top: 40px; font-size: 11.5px; line-height: 1.3; color: var(--on-red-soft); }
  .contact { list-style: none; margin-top: 10px; font-size: 11.5px; line-height: 1.4; color: var(--on-red-soft); }
  .contact li { display: flex; align-items: center; gap: 6px; }
  .contact svg { width: 10px; height: 10px; fill: var(--on-red); flex: none; }
  .contact .spacer { width: 10px; flex: none; }
  .website { margin-top: auto; font-weight: 700; font-size: 12px; letter-spacing: .2px; }

  /* Back */
  .card--back {
    background: var(--brand-red);
    color: var(--on-red);
    display: flex;
    flex-direction: column;
    align-items: center;
    justify-content: center;
  }
  .back__brand {
    font-family: "Archivo", Arial, sans-serif;
    font-weight: 800;
    font-size: 44px;
    line-height: 1.02;
    text-align: center;
  }
  .back__website {
    position: absolute;
    bottom: 18px;
    font-size: 13px;
    letter-spacing: .3px;
  }
</style>
</head>
<body>
  <section class="card card--back" aria-label="Card back">
    <div class="back__brand">The Copper<br>Lantern</div>
    <div class="back__website">www.TheCopperLantern.com</div>
  </section>

  <section class="card card--front" aria-label="Card front">
    <div class="front__brand">
      <span class="brand-square"></span>
      <div class="brand-name">The<br>Copper<br>Lantern</div>
    </div>
    <div class="front__divider"></div>
    <div class="front__details">
      <div class="person-name">Damon Fairley</div>
      <p class="address">417 W. Marlow Avenue, Apt 118<br>Ann Arbor, MI 48177</p>
      <ul class="contact">
        <li>
          <svg viewBox="0 0 10 10" aria-hidden="true"><path d="M2 0.5h2l.6 2.4-1.2.9a5.5 5.5 0 0 0 2.8 2.8l.9-1.2 2.4.6v2C9.5 9 9 9.5 8 9.5 4 9.5.5 6 .5 2 .5 1 1 .5 2 .5z"/></svg>
          586.314.2290
        </li>
        <li><span class="spacer"></span>419.552.0817</li>
        <li>
          <svg viewBox="0 0 10 10" aria-hidden="true"><path d="M0 2h10v6H0z M0.6 2.3 5 5.6 9.4 2.3" fill="none" stroke="#fff" stroke-width="1"/></svg>
          Damon@DamonFairley.com
        </li>
      </ul>
      <div class="website">www.TheCopperLantern.com</div>
    </div>
  </section>
</body>
</html>
```